World travel poster - I want to remember where I've been!

I would like a poster for me to print and keep in my home as a record of my world travels. It must look like a mechanical sign in an airport (see picture for example) However I am flexible with exact layout, if you'd like to add images used to enhance poster etc. I have also uploaded some pictures from my travels if you would like to use some or all of them. They are named according to location.

Poster must include:
USA 2003
Malaysia 2006
Thailand 2007
Italy 2009
India, Vietnam, Hong Kong 2010
Bali 2011
Malaysia 2012
Singapore 2012
Vietnam, Cambodia, Laos 2013
Europe 2015

and the quote:

"The world is a book and those who do not travel read only one page."
― Severin of Tallowmere
Updates

Hi there. I have uploaded some photos of my travels to possibly use in my poster. They are named according to location. I haven't decided if I prefer the originial layout or with images, so please post both for me to consider. Thanks so much for your time to consider my project.

Target Market(s)

Something to catch the eye of visitors and remind me of my adventures.
A classic piece that is a conversation starter.

Industry/Entity Type

Airport

Other font styles liked:
• Airport mechanical font

Requirements
Must have
• Some lettering like a mechanical airport board (see image attached for example).
Dimensions that are easy to print - either A3, or a long/narrow poster.
Nice to have
• A splash of colour or an image, maybe the words 'arrivals' or 'departures'

Use of some of my pictures if it doesn't look too busy.
Should not have
• Anything too over the top.

```html
<!DOCTYPE html>
<html lang="en">
<head>
<meta charset="utf-8">
<title>Departures – Travel Record</title>
<link href="https://fonts.googleapis.com/css2?family=Oswald:wght@400;600&family=Roboto:wght@400&display=swap" rel="stylesheet">
<style>
  :root {
    --header-top: #2a2a2a;
    --header-bottom: #0c0c0c;
    --tile-light: #3a3a3a;
    --tile-mid: #222222;
    --tile-dark: #121212;
    --gap: #060606;
    --label: #ffffff;
    --destination: #f2e21a;
    --date: #f07a12;
    --flap-text: #f4f4f4;
    --lamp-off: #bdbdbd;
    --lamp-on: #e8102a;
  }
  * { margin: 0; padding: 0; box-sizing: border-box; }
  html, body { width: 1200px; height: 778px; overflow: hidden; background: #000; }
  .board {
    position: relative; width: 1200px; height: 778px; overflow: hidden;
    font-family: "Oswald", "Arial Narrow", sans-serif;
  }
  .board-header {
    position: absolute; left: 0; top: 0; width: 1200px; height: 112px;
    background: linear-gradient(180deg, var(--header-top), var(--header-bottom));
  }
  .plane-icon { position: absolute; left: 28px; top: 30px; width: 41px; height: 41px; }
  .board-title {
    position: absolute; left: 89px; top: 20px; color: var(--label);
    font-family: "Roboto", Arial, sans-serif; font-size: 28px; font-weight: 400;
  }
  .column-label {
    position: absolute; top: 78px; color: var(--label);
    font-family: "Roboto", Arial, sans-serif; font-size: 16px; letter-spacing: -0.2px;
  }
  .flap-field {
    position: absolute; left: 0; top: 112px; width: 1200px; height: 628px;
    background-color: var(--tile-dark);
    background-image:
      repeating-linear-gradient(90deg, var(--gap) 0 2px, transparent 2px 19.6px),
      repeating-linear-gradient(180deg, var(--gap) 0 2px, transparent 2px 18px, rgba(0,0,0,.85) 18px 19.5px, transparent 19.5px 37px),
      repeating-linear-gradient(180deg, var(--tile-light) 0, var(--tile-mid) 18px, #2e2e2e 19.5px, var(--tile-dark) 37px);
    background-position: 0 12px;
  }
  .board-footer {
    position: absolute; left: 0; top: 740px; width: 1200px; height: 38px;
    background: linear-gradient(180deg, #1a1a1a, #2b2b2b);
  }
  .flap-text {
    position: absolute; line-height: 36px; white-space: nowrap;
    text-shadow: 0 1px 1px rgba(0,0,0,.8);
  }
  .flight-code { left: 52px; top: 188px; color: var(--flap-text); font-size: 26px; font-weight: 400; letter-spacing: 8.2px; }
  .status-lamp { position: absolute; top: 200px; width: 14px; height: 14px; border-radius: 50%; }
  .status-lamp.off { left: 203px; background: radial-gradient(circle at 40% 35%, #fff, var(--lamp-off) 60%, #555); }
  .status-lamp.on { left: 224px; background: radial-gradient(circle at 40% 35%, #ff8a8a, var(--lamp-on) 60%, #700); }
  .destination { left: 289px; color: var(--destination); font-size: 31px; font-weight: 600; letter-spacing: 6.9px; }
  .date { left: 876px; color: var(--date); font-size: 31px; font-weight: 600; letter-spacing: 4px; }
  .quote, .attribution { color: var(--flap-text); font-size: 24px; font-weight: 400; }
  .quote { left: 183px; letter-spacing: 11.5px; }
  .attribution { left: 705px; top: 668px; letter-spacing: 8px; }
</style>
</head>
<body>
<main class="board">
  <header class="board-header">
    <svg class="plane-icon" viewBox="0 0 41 41" aria-hidden="true">
      <rect width="41" height="41" rx="7" fill="#fff"/>
      <path d="M8 27 h25 v2 H8z M9 21 l3-1 4 3 5-2-7-8 3-1 10 6 6-2 c2-.6 3 1.6 1 2.4 L14 26 z" fill="#111"/>
    </svg>
    <div class="board-title">Departures</div>
    <div class="column-label" style="left:91px">FLIGHT</div>
    <div class="column-label" style="left:196px">STATUS</div>
    <div class="column-label" style="left:292px">DESTINATION</div>
    <div class="column-label" style="left:880px;top:81px">DATE</div>
    <div class="column-label" style="left:990px;top:81px">GATE</div>
    <div class="column-label" style="left:1075px;top:81px">TIME</div>
  </header>

  <section class="flap-field" aria-label="Travel record"></section>

  <div class="flap-text flight-code">TLW07Q</div>
  <span class="status-lamp off"></span>
  <span class="status-lamp on"></span>

  <div class="flap-text destination" style="top:150px">USA</div>
  <div class="flap-text date" style="top:150px">2003</div>
  <div class="flap-text destination" style="top:187px">MALAYSIA</div>
  <div class="flap-text date" style="top:187px">2006</div>
  <div class="flap-text destination" style="top:224px">THAILAND</div>
  <div class="flap-text date" style="top:224px">2007</div>
  <div class="flap-text destination" style="top:261px">ITALY</div>
  <div class="flap-text date" style="top:261px">2009</div>
  <div class="flap-text destination" style="top:299px">INDIA VIETNAM HONG KONG</div>
  <div class="flap-text date" style="top:299px">2010</div>
  <div class="flap-text destination" style="top:335px">BALI</div>
  <div class="flap-text date" style="top:335px">2011</div>
  <div class="flap-text destination" style="top:371px">MALAYSIA</div>
  <div class="flap-text date" style="top:371px">2012</div>
  <div class="flap-text destination" style="top:409px">SINGAPORE</div>
  <div class="flap-text date" style="top:409px">2012</div>
  <div class="flap-text destination" style="top:446px">VIETNAM CAMBOGIA LAOS</div>
  <div class="flap-text date" style="top:446px">2013</div>
  <div class="flap-text destination" style="top:482px">EUROPE</div>
  <div class="flap-text date" style="top:482px">2015</div>

  <div class="flap-text quote" style="top:557px">THE WORLD IS A BOOK AND THOSE WHO DO</div>
  <div class="flap-text quote" style="top:594px">NOT TRAVEL READ ONLY ONE PAGE</div>
  <div class="flap-text attribution">SEVERIN OF TALLOWMERE</div>

  <footer class="board-footer"></footer>
</main>
</body>
</html>
```